SHOP PAGE PRODUCT GRAPHICS 900x600 FOR E COMMERCE SITE. 5 TOTAL

NEED 5 GRAPHICS 900x600 MADE FOR MY SHOP PAGE HERE:

feel free to omit any redundant content http://pixelcratehub.com/qx/dorian/shop.jpg Custom Image For Products On Shop Page:AL A CARTE:Buy Video Ads On an As Needed Basis$37 PER VIDEO!INCLUDES:1 Video Ad ($149 VALUE) 1 Video Ad Converted To Square Ratio ($39 VALUE)1 Video Ad Converted To Vertical Ratio ($39 VALUE)1 Video Ad Converted To Chatterly Cover Video ($129 VALUE)VALUE $3564 Videos NOW ONLY $14960% OFF$37 PER VIDEO!INSTRUCTIONS FOR IMAGE:SHOW PHOTOS OF ALL PHOTOS SIZES USING SAME VIDEO. LET ME KNOW IF YOU NEED ONE I HAVE MP4 FILES FOR ALL SIZES SHOW PHOTOS OF ALL PHOTOS SIZES USING SAME VIDEO. LET ME KNOW IF YOU NEED ONE I HAVE MP4 FILES FOR ALL SIZES OR YOU CAN USE IMAGES FROM MY WEBSITE WWW.LARKREELSTUDIO.COM PLEASE SCROLL DOWN ON HOMEPAGE AND SEE “VIDEO SIZES” SECTION AND USE THESE IMAGES IF YOU HAVE TO….I WANT THE IMAGE TO SHOW ALL THE DIFFERENT VIDEO SIZES THEY GET SO IT LOOKS LIKE A LOT OF VALUE…._______________________________________________________________________________________SUBSCRIPTION:Big Discounts Per Video When You Sign Up For A Monthly Subscription$25 PER VIDEO!INCLUDES:1 Video Ad ($149 VALUE)1 Video Ad Converted To Square Ratio ($39 VALUE)1 Video Ad Converted To Vertical Ratio ($39 VALUE)1 Video Ad Converted To Chatterly Cover Video ($129 VALUE)VALUE $3564 Videos NOW ONLY $9975% OFF$25 PER VIDEO!INSTRUCTIONS FOR IMAGE:SHOW PHOTOS OF ALL PHOTOS SIZES USING SAME VIDEO. LET ME KNOW IF YOU NEED ONE I HAVE MP4 FILES FOR ALL SIZES SHOW PHOTOS OF ALL PHOTOS SIZES USING SAME VIDEO. LET ME KNOW IF YOU NEED ONE I HAVE MP4 FILES FOR ALL SIZES OR YOU CAN USE IMAGES FROM MY WEBSITE WWW.LARKREELSTUDIO.COM PLEASE SCROLL DOWN ON HOMEPAGE AND SEE “VIDEO SIEZES” SECTION AND USE THESE IMAGES IF YOU HAVE TO….I WANT THE IMAGE TO SHOW ALL THE DIFFERENT VIDEO SIZES THEY GET SO IT LOOKS LIKE A LOT OF VALUE….___________________________________________________________________________LARK MONTHLY CONTENT CALENDAR SUBSCRIPTION:Daily Content and Custom Branded Videos For Every Day.LESS THAN $10 PER VIDEO!INCLUDES:30 Videos ($1470 VALUE)VALUE $1470/mth30 Videos & Daily Content Only $299/mth90% OFF$10 PER VIDEO!INSTRUCTIONS FOR IMAGE:SHOW A PIC OF A CALENDAR WITH CONTENT/TEXT AND VIDEO FOR EACH DAY. SEE MY WEBSITE AT https://larkreelstudio.com/calendar/june and use something from here for this image. I WANT IT TO BE CLEAR THAT THEY WILL RECEIVE A VIDEO FOR EVERY DAY AND CONTENT TO POST TO THEIR SOCIAL MEDIA PAGES ______________________________________________________________________________HOLIDAY THEMED PACKAGECelebrate the Holidays with videos$58 PER VIDEO!INCLUDES:17 HOLIDAY THEMED VIDEOS ($1683 VALUE)VALUE $168317 Videos Only $99935% OFF$58 PER VIDEO!INSTRUCTIONS FOR IMAGE:SHOW A COLLAGE OF HOLIDAY THEMED VIDEOS. YOU CAN FIND SOME HOLIDAY THEMED VIDEOS ON MY WEBSITE HERE: https://larkreelstudio.com/categories FROM DROP DOWN MENU CHOOSE LABOR DAY, MEMORIAL DAY, HALLOWEEN, CHRISTMAS, NEW YEARS, NEW YEARS, VALENTINES TO SEE EXAMPLES OF HOLIDAY THEMED VIDEOS FOR THIS IMAGE. __________________________________________________________________SEASONAL THEMED PACKAGEWelcome every season with a new video$74 PER VIDEO!4 Seasonal Themed Videos ($396 VALUE)VALUE $3964 Videos Only $29925% OFF$74 PER VIDEO!INSTRUCTIONS FOR IMAGE:SHOW A COLLAGE OF SEASONAL THEMED VIDEOS. YOU CAN FIND THE SEASONAL THEMED VIDEOS ON MY WEBSITE CLIPNEST PAGE HERE: https://clipnest.com/user41527093 SUMMER, SPRING, FALL, WINTER

Target Market(s)

B2B

Industry/Entity Type

Video Production

Colors

Designer to choose colors to be used in the design.

Requirements
Must have
• NEED 5 GRAPHICS MADE FOR MY SHOP PAGE HERE: 900x600 ://pixelcratehub.com/qx/dorian/shop.jpg
• Custom Image For Products On Shop Page:
• AL A CARTE:
• Buy Video Ads On an As Needed Basis
• $37 PER VIDEO!
• INCLUDES:
• 1 Video Ad ($149 VALUE)
• 1 Video Ad Converted To Square Ratio ($39 VALUE)
• 1 Video Ad Converted To Vertical Ratio ($39 VALUE)
• 1 Video Ad Converted To Chatterly Cover Video ($129 VALUE)
• VALUE $356
• 4 Videos NOW ONLY $149
• 60% OFF
• $37 PER VIDEO!
• INSTRUCTIONS FOR IMAGE:
• SHOW PHOTOS OF ALL PHOTOS SIZES USING SAME VIDEO. LET ME KNOW IF YOU NEED ONE I HAVE MP4 FILES FOR ALL SIZES SHOW PHOTOS OF ALL PHOTOS SIZES USING SAME VIDEO. LET ME KNOW IF YOU NEED ONE I HAVE MP4 FILES FOR ALL SIZES OR YOU CAN USE IMAGES FROM MY WEBSITE WWW.LARKREELSTUDIO.COM PLEASE SCROLL DOWN ON HOMEPAGE AND SEE “VIDEO SIZES” SECTION AND USE THESE IMAGES IF YOU HAVE TO….I WANT THE IMAGE TO SHOW ALL THE DIFFERENT VIDEO SIZES THEY GET SO IT LOOKS LIKE A LOT OF VALUE….
• _______________________________________________________________________________________
• SUBSCRIPTION:
• Big Discounts Per Video When You Sign Up For A Monthly Subscription
• $25 PER VIDEO!
• INCLUDES:
• 1 Video Ad ($149 VALUE)
• VALUE $356
• 4 Videos NOW ONLY $99
• 75% OFF
• $25 PER VIDEO!
• INSTRUCTIONS FOR IMAGE:
• SHOW PHOTOS OF ALL PHOTOS SIZES USING SAME VIDEO. LET ME KNOW IF YOU NEED ONE I HAVE MP4 FILES FOR ALL SIZES SHOW PHOTOS OF ALL PHOTOS SIZES USING SAME VIDEO. LET ME KNOW IF YOU NEED ONE I HAVE MP4 FILES FOR ALL SIZES OR YOU CAN USE IMAGES FROM MY WEBSITE WWW.LARKREELSTUDIO.COM PLEASE SCROLL DOWN ON HOMEPAGE AND SEE “VIDEO SIEZES” SECTION AND USE THESE IMAGES IF YOU HAVE TO….I WANT THE IMAGE TO SHOW ALL THE DIFFERENT VIDEO SIZES THEY GET SO IT LOOKS LIKE A LOT OF VALUE….
• ___________________________________________________________________________
• LARK MONTHLY CONTENT CALENDAR SUBSCRIPTION:
• Daily Content and Custom Branded Videos For Every Day.
• LESS THAN $10 PER VIDEO!
• INCLUDES:
• 30 Videos ($1470 VALUE)
• VALUE $1470/mth
• 30 Videos & Daily Content Only $299/mth
• 90% OFF
• $10 PER VIDEO!
• INSTRUCTIONS FOR IMAGE:
• SHOW A PIC OF A CALENDAR WITH CONTENT/TEXT AND VIDEO FOR EACH DAY. SEE MY WEBSITE AT https://larkreelstudio.com/calendar/june and use something from here for this image. I WANT IT TO BE CLEAR THAT THEY WILL RECEIVE A VIDEO FOR EVERY DAY AND CONTENT TO POST TO THEIR SOCIAL MEDIA PAGES
• ______________________________________________________________________________
• HOLIDAY THEMED PACKAGE
• Celebrate the Holidays with videos
• $58 PER VIDEO!
• INCLUDES:
• 17 HOLIDAY THEMED VIDEOS ($1683 VALUE)
• VALUE $1683
• 17 Videos Only $999
• 35% OFF
• $58 PER VIDEO!
• INSTRUCTIONS FOR IMAGE:
• SHOW A COLLAGE OF HOLIDAY THEMED VIDEOS. YOU CAN FIND SOME HOLIDAY THEMED VIDEOS ON MY WEBSITE HERE: https://larkreelstudio.com/categories FROM DROP DOWN MENU CHOOSE LABOR DAY, MEMORIAL DAY, HALLOWEEN, CHRISTMAS, NEW YEARS, NEW YEARS, VALENTINES TO SEE EXAMPLES OF HOLIDAY THEMED VIDEOS FOR THIS IMAGE.
• __________________________________________________________________
• SEASONAL THEMED PACKAGE
• Welcome every season with a new video
• $74 PER VIDEO!
• 4 Seasonal Themed Videos ($396 VALUE)
• VALUE $396
• 4 Videos Only $299
• 25% OFF
• $74 PER VIDEO!
• INSTRUCTIONS FOR IMAGE:
• SHOW A COLLAGE OF SEASONAL THEMED VIDEOS. YOU CAN FIND THE SEASONAL THEMED VIDEOS ON MY WEBSITE CLIPNEST PAGE HERE: https://clipnest.com/user41527093 SUMMER, SPRING, FALL, WINTER
Nice to have
• NEED 5 GRAPHICS MADE FOR MY SHOP PAGE HERE: http://pixelcratehub.com/qx/dorian/shop.jpg 900x600
• AL A CARTE:
• $37 PER VIDEO!
• INCLUDES:
• 1 Video Ad ($149 VALUE)
• VALUE $356
• 4 Videos NOW ONLY $149
• 60% OFF
• $37 PER VIDEO!
• INSTRUCTIONS FOR IMAGE:
• SUBSCRIPTION:
• $25 PER VIDEO!
• INCLUDES:
• 1 Video Ad ($149 VALUE)
• VALUE $356
• 4 Videos NOW ONLY $99
• 75% OFF
• $25 PER VIDEO!
• INSTRUCTIONS FOR IMAGE:
• INCLUDES:
• 30 Videos ($1470 VALUE)
• VALUE $1470/mth
• 90% OFF
• $10 PER VIDEO!
• INSTRUCTIONS FOR IMAGE:
• HOLIDAY THEMED PACKAGE
• $58 PER VIDEO!
• INCLUDES:
• VALUE $1683
• 17 Videos Only $999
• 35% OFF
• $58 PER VIDEO!
• INSTRUCTIONS FOR IMAGE:
• SEASONAL THEMED PACKAGE
• $74 PER VIDEO!
• VALUE $396
• 4 Videos Only $299
• 25% OFF
• $74 PER VIDEO!
• INSTRUCTIONS FOR IMAGE:
Should not have
• AL A CARTE:
• $37 PER VIDEO!
• INCLUDES:
• 1 Video Ad ($149 VALUE)
• VALUE $356
• 4 Videos NOW ONLY $149
• 60% OFF
• $37 PER VIDEO!
• INSTRUCTIONS FOR IMAGE:
• SUBSCRIPTION:
• $25 PER VIDEO!
• INCLUDES:
• 1 Video Ad ($149 VALUE)
• VALUE $356
• 4 Videos NOW ONLY $99
• 75% OFF
• $25 PER VIDEO!
• INSTRUCTIONS FOR IMAGE:
• INCLUDES:
• 30 Videos ($1470 VALUE)
• VALUE $1470/mth
• 90% OFF
• $10 PER VIDEO!
• INSTRUCTIONS FOR IMAGE:
• HOLIDAY THEMED PACKAGE
• $58 PER VIDEO!
• INCLUDES:
• VALUE $1683
• 17 Videos Only $999
• 35% OFF
• $58 PER VIDEO!
• INSTRUCTIONS FOR IMAGE:
• SEASONAL THEMED PACKAGE
• $74 PER VIDEO!
• VALUE $396
• 4 Videos Only $299
• 25% OFF
• $74 PER VIDEO!
• INSTRUCTIONS FOR IMAGE:

```html
<!DOCTYPE html>
<html lang="en">
<head>
<meta charset="utf-8">
<title>Holiday Themed Package</title>
<link rel="stylesheet" href="https://fonts.googleapis.com/css2?family=Lobster&family=Oswald:wght@700&family=Montserrat:wght@400;700&display=swap">
<style>
  :root {
    --stage: #d6d7d9;
    --wood-light: #e6c9a3;
    --wood-mid: #d9b68a;
    --tile-edge: #ffffff;
    --play: rgba(255, 255, 255, 0.92);
    --valentine-purple: #b98ce8;
    --labor-blue: #1d3f9c;
    --deal-white: #ffffff;
    --caption-cream: #f3ead9;
    --logo-white: #eef2ff;
  }
  * { margin: 0; padding: 0; box-sizing: border-box; }
  html, body { width: 1200px; height: 869px; overflow: hidden; }
  body { background: var(--stage); position: relative; }

  .shop-graphic {
    position: absolute; left: 0; top: 34px; width: 1200px; height: 800px;
    background: linear-gradient(160deg, var(--wood-light) 0%, var(--wood-mid) 55%, var(--wood-light) 100%);
    overflow: hidden;
  }

  .video-tile {
    position: absolute;
    border: 2px solid var(--tile-edge);
    box-shadow: 0 4px 12px rgba(0, 0, 0, 0.35);
    overflow: hidden;
  }
  .video-tile .still { position: absolute; inset: 0; }
  .play-icon { position: absolute; width: 44px; height: 52px; }

  /* Valentine's Day */
  .tile-valentine { left: 35px; top: 37px; width: 604px; height: 340px; z-index: 3; }
  .tile-valentine .still { background: radial-gradient(circle at 30% 20%, #fff7ee 0%, #f7d2c4 30%, #d98b86 65%, #8a5a5e 100%); }
  .valentine-my {
    position: absolute; left: 10px; top: 83px; padding: 2px 16px 8px;
    background: var(--valentine-purple); color: #fff;
    font: 58px "Lobster", cursive; transform: rotate(-8deg);
  }
  .valentine-word {
    position: absolute; left: 36px; top: 160px;
    font: 42px "Lobster", cursive; color: #2b2b2b; transform: rotate(-10deg);
  }
  .tile-logo {
    position: absolute; font: 700 13px "Montserrat", sans-serif;
    color: var(--logo-white); letter-spacing: 1px;
  }

  /* Labor Day */
  .tile-labor { left: 708px; top: 28px; width: 448px; height: 344px; z-index: 4; }
  .tile-labor .still { background: linear-gradient(180deg, #f7f8fa 0%, #eceef2 62%, #1f47b8 63%, #1f47b8 70%, #e8e8ea 71%, #d9d9dc 100%); }
  .labor-headline {
    position: absolute; left: 36px; top: 44px;
    font: 700 60px/1.05 "Oswald", sans-serif; color: var(--labor-blue);
    text-transform: uppercase; transform: scaleX(0.82); transform-origin: left;
  }

  /* Summer / Memorial */
  .tile-summer { left: 457px; top: 255px; width: 460px; height: 259px; z-index: 5; }
  .tile-summer .still { background: linear-gradient(180deg, #dfeef2 0%, #8fc3c9 30%, #2f8a8c 60%, #1e6b6c 100%); }
  .summer-caption {
    position: absolute; left: 0; right: 0; bottom: 30px; text-align: center;
    font: 58px "Lobster", cursive; color: #fff;
    text-shadow: 0 2px 6px rgba(0, 0, 0, 0.35);
  }

  /* Black Friday deals */
  .tile-deals { left: 28px; top: 449px; width: 569px; height: 319px; z-index: 1; }
  .tile-deals .still { background: radial-gradient(circle at 55% 40%, #5a1f17 0%, #2a1412 40%, #111 80%); }
  .deals-headline {
    position: absolute; left: 22px; bottom: 18px;
    font: 700 38px/1.08 "Oswald", sans-serif; color: var(--deal-white);
    text-transform: uppercase; transform: scaleX(0.85); transform-origin: left;
  }

  /* Boxing Day */
  .tile-boxing { left: 621px; top: 476px; width: 556px; height: 307px; z-index: 2; }
  .tile-boxing .still { background: radial-gradient(circle at 50% 30%, #d9a98a 0%, #8a5a3e 45%, #3a2418 100%); }
  .boxing-band {
    position: absolute; left: 0; right: 0; bottom: 0; height: 62px;
    background: linear-gradient(180deg, #6a4a2c 0%, #4c3520 100%);
  }
  .boxing-caption {
    position: absolute; right: 100px; bottom: 12px;
    font: 400 35px "Montserrat", sans-serif; color: var(--caption-cream); letter-spacing: 1px;
  }
</style>
</head>
<body>
  <main class="shop-graphic" aria-label="Holiday themed package video collage">

    <article class="video-tile tile-valentine">
      <div class="still" role="img" aria-label="Couple on a bicycle at sunset by the sea"></div>
      <span class="valentine-my">My</span>
      <span class="valentine-word">Valentine?</span>
      <span class="tile-logo" style="left:26px; top:272px;">LARK</span>
      <svg class="play-icon" style="left:282px; top:114px;" viewBox="0 0 44 52"><path d="M0 0 L44 26 L0 52 Z" fill="var(--play)"/></svg>
    </article>

    <article class="video-tile tile-labor">
      <div class="still" role="img" aria-label="Worker in a hard hat cheering in an empty room"></div>
      <div class="labor-headline">No Labor<br>Allowed</div>
      <svg class="play-icon" style="left:204px; top:120px;" viewBox="0 0 44 52"><path d="M0 0 L44 26 L0 52 Z" fill="var(--play)"/></svg>
    </article>

    <article class="video-tile tile-deals">
      <div class="still" role="img" aria-label="Hands passing a wrapped gift across a dark table"></div>
      <div class="deals-headline">The Best Deals<br>Seem to Appear!</div>
      <svg class="play-icon" style="left:534px; top:0; left:246px; top:124px;" viewBox="0 0 44 52"><path d="M0 0 L44 26 L0 52 Z" fill="var(--play)"/></svg>
    </article>

    <article class="video-tile tile-boxing">
      <div class="still" role="img" aria-label="Family gathered around looking excited on Boxing Day"></div>
      <div class="boxing-band"></div>
      <span class="tile-logo" style="left:2px; bottom:22px;">LARK</span>
      <span class="boxing-caption">Boxing Day</span>
      <svg class="play-icon" style="left:262px; top:130px;" viewBox="0 0 44 52"><path d="M0 0 L44 26 L0 52 Z" fill="var(--play)"/></svg>
    </article>

    <article class="video-tile tile-summer">
      <div class="still" role="img" aria-label="Swimmer in the ocean under bright sun"></div>
      <span class="summer-caption">Set You Free</span>
      <svg class="play-icon" style="left:364px; top:0; left:214px; top:90px;" viewBox="0 0 44 52"><path d="M0 0 L44 26 L0 52 Z" fill="var(--play)"/></svg>
    </article>

  </main>
</body>
</html>
```